Business Card/Email Signature design

We need an new business card design for our business as well as an animated email signature design.<br/>Business Card:<br/>The business card designs need to have the following information for each director:<br/>Leon Bramwell<br/>Managing Director<br/>leon@talvoraworks.com.au<br/>0498617340<br/>www.talvoraworks.com.au<br/><br/>and<br/><br/>Priscilla Venton<br/>Director<br/>priscilla@talvoraworks.com.au<br/>0467302958<br/>www.talvoraworks.com.au<br/><br/>I will upload the Talvora. Works logo designs to be used for the design. Our colours are black and white. I would like to see the designs in both coloured backgrounds.<br/><br/>For the email signature we need the same information. I also need to add a logo of our association BLPX of which i will add the logo as well. This BLPX logo does not need to be used for the business card unless it works with the design.<br/>For the animation part of the logo our company is called Talvora. Works - We have a number of divisions called Talvora. Construct, Talvora. Property, Talvora. Sales, Talvora. Executive Support, Talvora. Private PA, Talvora. Talent and Talvora. Coaching<br/>I would like for the email Signature to be designed so that the Talvora. stays still but the words Construct, Property, Sales, Executive Support, Private PA, Talent and Coaching rotate through to capture attention and tell the story of what we do.<br/><br/>Any questions please don't hesitate to message me.

Industry/Entity Type

Recruiter

Contact Information for Business Card

Leon Bramwell
Managing Director
leon@talvoraworks.com.au
0498617340
www.talvoraworks.com.au

Priscilla Venton
Director
priscilla@talvoraworks.com.au
0467302958
www.talvoraworks.com.au

Font styles to use
Serif

Colors

Designer to choose colors to be used in the design.

Requirements
Must have
• The animation for the email signature as described
Should not have
• Any changes to my logo. Any colour other that black or white

```html
<!DOCTYPE html>
<html lang="en">
<head>
<meta charset="utf-8">
<title>Talvora. Works – Business Card</title>
<link href="https://fonts.googleapis.com/css2?family=Cormorant+Garamond:wght@600&family=Roboto:wght@400;700&family=Montserrat:wght@400&display=swap" rel="stylesheet">
<style>
  :root {
    --ink: #121212;
    --paper: #ffffff;
    --grey: #6a6a6a;
    --stage: #ffffff;
    --shadow: rgba(0,0,0,0.28);
  }
  html, body {
    margin: 0;
    padding: 0;
    width: 1200px;
    height: 1200px;
    overflow: hidden;
    background: var(--stage);
  }
  .canvas { position: relative; width: 1200px; height: 1200px; }

  .card {
    position: absolute;
    box-shadow: 0 10px 28px var(--shadow);
  }
  .card--front {
    left: 174px; top: 46px; width: 856px; height: 513px;
    background: var(--ink);
    color: var(--paper);
  }
  .card--back {
    left: 177px; top: 620px; width: 853px; height: 511px;
    background: var(--paper);
    color: var(--ink);
  }

  .brand-frame {
    position: absolute;
    box-sizing: border-box;
  }
  .card--front .brand-frame {
    left: 162px; top: 183px; width: 240px; height: 146px;
    border: 1.5px solid var(--paper);
  }
  .card--back .brand-frame {
    left: 73px; top: 142px; width: 243px; height: 126px;
    border: 1.5px solid var(--ink);
  }

  .brand-name {
    position: absolute;
    margin: 0;
    font-family: "Cormorant Garamond", serif;
    font-weight: 600;
    text-transform: uppercase;
    letter-spacing: 1px;
    line-height: 1.1;
    text-align: center;
  }
  .card--front .brand-name {
    left: 427px; top: 226px; width: 268px;
    font-size: 40px;
    color: var(--paper);
  }
  .card--back .brand-name {
    left: 73px; top: 278px; width: 243px;
    font-size: 38px;
    color: var(--ink);
  }

  .divider {
    position: absolute;
    left: 353px; top: 138px;
    width: 2px; height: 221px;
    background: var(--ink);
  }

  .person {
    position: absolute;
    left: 389px; top: 140px;
  }
  .person__name {
    margin: 0;
    font-family: "Roboto", sans-serif;
    font-weight: 700;
    font-size: 29px;
    letter-spacing: 0.3px;
    line-height: 1;
  }
  .person__role {
    margin: 10px 0 0;
    font-family: "Roboto", sans-serif;
    font-weight: 700;
    font-size: 19px;
    color: var(--grey);
  }
  .person__division {
    margin: 8px 0 0;
    font-family: "Roboto", sans-serif;
    font-weight: 400;
    font-size: 18px;
    color: var(--grey);
  }

  .contact {
    list-style: none;
    margin: 34px 0 0;
    padding: 0;
    font-family: "Montserrat", sans-serif;
    font-size: 20px;
    color: var(--ink);
  }
  .contact__item {
    display: flex;
    align-items: center;
    height: 32px;
  }
  .contact__icon {
    width: 20px; height: 20px;
    margin-right: 9px;
    flex: none;
  }
</style>
</head>
<body>
<main class="canvas">

  <section class="card card--front" aria-label="Card front">
    <div class="brand-frame"></div>
    <p class="brand-name">Talvora.<br>Works</p>
  </section>

  <section class="card card--back" aria-label="Card back">
    <div class="brand-frame"></div>
    <p class="brand-name">Talvora.<br>Works</p>

    <div class="divider"></div>

    <div class="person">
      <h1 class="person__name">MARISOL DENTRY</h1>
      <p class="person__role">Director</p>
      <p class="person__division">Executive Support Division</p>

      <ul class="contact">
        <li class="contact__item">
          <svg class="contact__icon" viewBox="0 0 24 24" aria-hidden="true">
            <path d="M6.6 10.8a15.1 15.1 0 0 0 6.6 6.6l2.2-2.2c.3-.3.7-.4 1-.2 1.1.4 2.3.6 3.6.6.6 0 1 .4 1 1V20c0 .6-.4 1-1 1A17 17 0 0 1 3 4c0-.6.4-1 1-1h3.5c.6 0 1 .4 1 1 0 1.3.2 2.5.6 3.6.1.3 0 .7-.2 1z" fill="currentColor"/>
            <path d="M14 3a7 7 0 0 1 7 7M14 6.5a3.5 3.5 0 0 1 3.5 3.5" fill="none" stroke="currentColor" stroke-width="1.8"/>
          </svg>
          <span>0452 718 306</span>
        </li>
        <li class="contact__item">
          <svg class="contact__icon" viewBox="0 0 24 24" aria-hidden="true">
            <path d="M2 5h20v14H2z" fill="currentColor"/>
            <path d="M2.5 5.5 12 13l9.5-7.5" fill="none" stroke="#fff" stroke-width="1.6"/>
          </svg>
          <span>marisol@talvoraworks.com.au</span>
        </li>
        <li class="contact__item">
          <svg class="contact__icon" viewBox="0 0 24 24" aria-hidden="true">
            <circle cx="12" cy="12" r="10" fill="currentColor"/>
            <path d="M7 7c2 1 3 0 4 2s-1 3 1 4 1 4 2 5M15 5c-1 2 1 3 3 3" fill="none" stroke="#fff" stroke-width="1.4"/>
          </svg>
          <span>www.talvoraworks.com.au</span>
        </li>
      </ul>
    </div>
  </section>

</main>
</body>
</html>
```